Powerpoint Slides for 'Lantern Ridge | consulting' firm

Hello,

I would like a suite of slides to not be typical of just ANOther deck. My business name is 'Lantern Ridge | consulting', so I would like to see innovation and creativity translated into the slides.

1. ‘Company/Cover Page’ – should showcase Lantern Ridge | consulting branding; perhaps with some animation to give the sense of 'out of the box' content.
The company name, Lantern Ridge | consulting, and tagline - Strategise | Organise | Optimise | Communicate, should appear together on the front and end page. The company name should appear on all other pages
2. Master branded background slide, with suggested font, and ideally with some colour options which could be leveraged in longer presentations to ‘break’ it up
3. Master branded background slide with an option to include bulleted content within some type of e.g. shape/form (not just as bullets against a blank background)
4. Divider slide (possibly leveraging some of the colours in Point 2

I have attached a copy of the logo/layout of my business card. The square used is raised on the business card which gives a very subtle effect of literally being out of the box. I would like something of a similar feel, but with colour (as noted in Point 2), though very open to ideas/suggestions.

Many Thanks,
Marisol
Updates

This project has been re-opened to all designers. I look forward to seeing creative and innovative submissions. Best Regards, Marisol

Target Market(s)

SMEs and Corporates - however, I don't want to look like just any other consultancy company.

Industry/Entity Type

Business

Colors

Designer to choose colors to be used in the design.

Requirements
Must have
• Innovation; Creativity; Professionalism; Succinct

```html
<!DOCTYPE html>
<html lang="en">
<head>
<meta charset="utf-8">
<title>Lantern Ridge | consulting – Slide Suite</title>
<link rel="stylesheet" href="https://fonts.googleapis.com/css2?family=Crimson+Pro:wght@400;500&display=swap">
<style>
  :root {
    --navy: #283891;
    --sky: #27a9e1;
    --paper: #ffffff;
    --ink: #111111;
    --stage: #d9dbde;
  }
  * { margin: 0; padding: 0; box-sizing: border-box; }
  html, body {
    width: 887px;
    height: 1200px;
    overflow: hidden;
    background: var(--stage);
  }
  .suite {
    position: relative;
    width: 887px;
    height: 1200px;
  }
  .slide {
    position: absolute;
    left: 63px;
    width: 760px;
    height: 550px;
    background: var(--navy);
    overflow: hidden;
  }
  .slide--cover { top: 35px; }
  .slide--about { top: 615px; }
  .slide svg { display: block; width: 100%; height: 100%; }
  .tile-edge { fill: var(--sky); }
  .tile-face { fill: var(--paper); stroke: var(--sky); stroke-width: 4; }
  .slide-text {
    font-family: "Crimson Pro", Georgia, serif;
    fill: var(--ink);
    text-anchor: middle;
    font-weight: 400;
  }
  .slide-text--brand { font-size: 21px; }
  .slide-text--brand-small { font-size: 18px; }
  .slide-text--headline { font-size: 23px; letter-spacing: 1px; font-weight: 500; }
  .slide-text--presenter { font-size: 20px; }
  .slide-text--title { font-size: 32px; }
</style>
</head>
<body>
<main class="suite">

  <section class="slide slide--cover" aria-label="Cover slide">
    <svg viewBox="0 0 760 550" xmlns="http://www.w3.org/2000/svg">
      <g transform="translate(560 115) rotate(40)">
        <rect class="tile-edge" x="-48" y="-40" width="96" height="96" rx="14"/>
        <rect class="tile-face" x="-48" y="-48" width="96" height="96" rx="14"/>
      </g>
      <g transform="translate(335 440) rotate(40)">
        <rect class="tile-edge" x="-38" y="-31" width="76" height="76" rx="10"/>
        <rect class="tile-face" x="-38" y="-38" width="76" height="76" rx="10"/>
      </g>
      <g transform="translate(295 470) rotate(40)">
        <rect class="tile-edge" x="-26" y="-20" width="52" height="52" rx="8"/>
        <rect class="tile-face" x="-26" y="-26" width="52" height="52" rx="8"/>
      </g>
      <g class="brand-tile" transform="translate(170 330) rotate(40)">
        <rect class="tile-edge" x="-88" y="-80" width="176" height="176" rx="20"/>
        <rect class="tile-face" x="-88" y="-88" width="176" height="176" rx="20"/>
      </g>
      <g transform="translate(610 400) rotate(40)">
        <rect class="tile-edge" x="-98" y="-90" width="196" height="196" rx="20"/>
        <rect class="tile-face" x="-98" y="-98" width="196" height="196" rx="20"/>
      </g>
      <g transform="translate(430 270) rotate(40)">
        <rect class="tile-edge" x="-150" y="-140" width="300" height="300" rx="30"/>
        <rect class="tile-face" x="-150" y="-150" width="300" height="300" rx="30"/>
      </g>
      <text class="slide-text slide-text--brand" x="150" y="330">Lantern Ridge</text>
      <text class="slide-text slide-text--brand" x="155" y="354">consulting</text>
      <text class="slide-text slide-text--headline" x="430" y="255">PRESENTATION</text>
      <text class="slide-text slide-text--headline" x="430" y="283">HEADLINE</text>
      <text class="slide-text slide-text--presenter" x="630" y="410">Presented by</text>
    </svg>
  </section>

  <section class="slide slide--about" aria-label="About slide">
    <svg viewBox="0 0 760 550" xmlns="http://www.w3.org/2000/svg">
      <g transform="translate(225 395) rotate(40)">
        <rect class="tile-edge" x="-36" y="-30" width="72" height="72" rx="10"/>
        <rect class="tile-face" x="-36" y="-36" width="72" height="72" rx="10"/>
      </g>
      <g transform="translate(185 450) rotate(40)">
        <rect class="tile-edge" x="-26" y="-20" width="52" height="52" rx="8"/>
        <rect class="tile-face" x="-26" y="-26" width="52" height="52" rx="8"/>
      </g>
      <g class="brand-tile" transform="translate(120 320) rotate(40)">
        <rect class="tile-edge" x="-78" y="-71" width="156" height="156" rx="18"/>
        <rect class="tile-face" x="-78" y="-78" width="156" height="156" rx="18"/>
      </g>
      <g transform="translate(620 300) rotate(40)">
        <rect class="tile-edge" x="-300" y="-285" width="600" height="600" rx="40"/>
        <rect class="tile-face" x="-300" y="-300" width="600" height="600" rx="40"/>
      </g>
      <text class="slide-text slide-text--brand-small" x="105" y="322">Lantern Ridge</text>
      <text class="slide-text slide-text--brand-small" x="108" y="344">consulting</text>
      <text class="slide-text slide-text--title" x="510" y="75">About</text>
      <text class="slide-text slide-text--title" x="545" y="110">Company details</text>
    </svg>
  </section>

</main>
</body>
</html>
```